Flyer Design Project

Family owned and operated roof repair, cleaning and restoration business. Offering quality service and product at a quality price. Have been in existence for over 25 years.
I have just had a logo designed for the business. I would like to generate business by getting people to look at their roof and consider the maintenance and appearance.
Must generate a serious approach as there have been some operators who have acted poorly.
We DO NOT pressure sell, but gladly provide quotes and advice. We only use the best quality products and we are a licensed applicator of this product.
Our finished product will protect homes and increase their value.
Target Market(s)
Home owners who have a house with concrete roof tiles.
Industry/Entity Type
Business
Look and feel

```html
<!DOCTYPE html>
<html lang="en">
<head>
<meta charset="utf-8">
<title>Dura-Crest Roof Restoration Flyer</title>
<link href="https://fonts.googleapis.com/css2?family=Roboto+Condensed:wght@700;800&family=Arimo:wght@400;700&family=Open+Sans:wght@400;700&display=swap" rel="stylesheet">
<style>
  :root {
    --page-bg: #e9e4dd;
    --ink-black: #0d0d0d;
    --brand-blue: #2f7aa6;
    --brand-blue-deep: #1d5479;
    --brand-blue-light: #5fa6d3;
    --white: #ffffff;
    --photo-red: #a8434a;
    --photo-grey: #c9c9c4;
  }
  * { margin: 0; padding: 0; box-sizing: border-box; }
  html, body { width: 1200px; height: 900px; overflow: hidden; background: var(--page-bg); }
  .flyer {
    position: absolute; left: 310px; top: 39px;
    width: 580px; height: 822px;
    background: linear-gradient(180deg, var(--brand-blue) 0%, var(--brand-blue-deep) 100%);
    box-shadow: 0 4px 14px rgba(0,0,0,.25);
    overflow: hidden;
  }
  .flyer-shapes { position: absolute; inset: 0; }
  .headline {
    position: absolute; left: 20px; top: 26px;
    font-family: "Roboto Condensed", "Arial Narrow", sans-serif;
    font-weight: 800; font-size: 21px; line-height: 27px;
    color: var(--white); letter-spacing: .1px;
  }
  .brand {
    position: absolute; right: 28px; top: 98px;
    display: flex; align-items: center; gap: 8px;
    font-family: "Roboto Condensed", "Arial Narrow", sans-serif;
    font-weight: 700; color: var(--white); text-align: left;
  }
  .brand-square { width: 14px; height: 14px; background: var(--white); }
  .brand-name { font-size: 30px; line-height: 30px; display: block; }
  .brand-sub { font-size: 15px; line-height: 16px; display: block; }
  .badge-text {
    position: absolute; left: 8px; top: 395px; width: 120px; height: 120px;
    display: flex; flex-direction: column; align-items: center; justify-content: center;
    transform: rotate(-20deg);
    font-family: "Arimo", Arial, sans-serif; font-weight: 700;
    color: var(--white); text-align: center; font-size: 14px; line-height: 16px;
    white-space: nowrap;
  }
  .badge-text .years { font-size: 18px; line-height: 21px; }
  .body-copy {
    position: absolute; left: 20px; right: 20px; top: 517px;
    font-family: "Arimo", Arial, sans-serif; font-size: 13px; line-height: 16.5px;
    color: var(--white); text-align: center;
  }
  .body-copy p { margin-bottom: 13px; }
  .contact-tab {
    position: absolute; left: 195px; top: 732px; width: 190px; height: 20px;
    font-family: "Open Sans", Arial, sans-serif; font-weight: 700; font-size: 14px;
    color: var(--white); text-align: center; line-height: 20px;
  }
  .contact-bar {
    position: absolute; left: 0; right: 0; top: 750px; height: 58px;
    display: flex; align-items: center;
    font-family: "Open Sans", Arial, sans-serif; font-size: 14px; line-height: 19px;
    color: var(--white); white-space: nowrap;
  }
  .contact-col { padding: 0 16px; }
  .contact-col + .contact-col { border-left: 1px solid rgba(255,255,255,.7); }
  .contact-address { padding-left: 17px; padding-right: 10px; width: 230px; }
  .contact-phone { width: 160px; }
</style>
</head>
<body>
<div class="flyer">
  <svg class="flyer-shapes" width="580" height="822" viewBox="0 0 580 822">
    <defs>
      <linearGradient id="photoTone" x1="0" y1="0" x2="1" y2="1">
        <stop offset="0" stop-color="var(--photo-red)"/>
        <stop offset=".5" stop-color="var(--photo-grey)"/>
        <stop offset="1" stop-color="var(--photo-red)"/>
      </linearGradient>
      <radialGradient id="badgeTone" cx=".4" cy=".35" r=".7">
        <stop offset="0" stop-color="var(--brand-blue-light)"/>
        <stop offset="1" stop-color="var(--brand-blue-deep)"/>
      </radialGradient>
    </defs>
    <path d="M0 0 H580 V140 C500 150 430 150 360 140 C250 120 150 85 60 90 C35 92 15 96 0 100 Z" fill="var(--ink-black)"/>
    <path d="M0 135 C120 110 240 135 340 165 C430 190 510 175 580 145 V165 C500 200 420 205 330 185 C230 160 110 150 0 165 Z" fill="var(--ink-black)"/>
    <path role="img" aria-label="Photo of a roofer in a hard hat laying red concrete roof tiles"
          d="M0 165 C110 150 230 160 330 185 C420 207 500 200 580 165 V470 C520 455 460 445 400 445 C300 445 200 470 120 500 C70 515 30 515 0 505 Z" fill="url(#photoTone)"/>
    <path d="M0 500 C40 512 80 508 130 492 C220 462 310 438 400 440 C470 442 530 455 580 470 V482 C520 468 460 460 400 460 C310 460 220 485 130 510 C80 522 40 522 0 515 Z" fill="var(--ink-black)"/>
    <circle cx="68" cy="455" r="66" fill="var(--white)" opacity=".85"/>
    <circle cx="68" cy="455" r="62" fill="url(#badgeTone)"/>
    <rect x="0" y="750" width="580" height="58" fill="var(--ink-black)"/>
    <path d="M205 730 H375 L390 750 H190 Z" fill="var(--ink-black)"/>
    <rect x="0" y="808" width="580" height="14" fill="var(--brand-blue)"/>
  </svg>

  <h1 class="headline">FAMILY OWNED AND OPERATED ROOF REPAIR,<br>CLEANING AND RESTORATION BUSINESS</h1>

  <div class="brand">
    <span class="brand-square"></span>
    <span><span class="brand-name">DURA-CREST</span><span class="brand-sub">Roof Restoration</span></span>
  </div>

  <div class="badge-text"><span>Have been in</span><span>existence</span><span>for over</span><span class="years">25 years.</span></div>

  <div class="body-copy">
    <p>Family owned and operated roof repair, cleaning and restoration business.<br>Offering quality service and product at a quality price.</p>
    <p>We would like to generate business by getting people to look at their roof and consider the maintenance and appearance. Must generate a serious approach as there have been some operators who have acted poorly.</p>
    <p>We DO NOT pressure sell, but gladly provide quotes and advice. We only use the best quality products and we are a licensed applicator of this product.</p>
    <p>Our finished product will protect homes and increase their value.</p>
  </div>

  <div class="contact-tab">CONTACT US TODAY</div>
  <div class="contact-bar">
    <div class="contact-col contact-address">your address goes here, Street ,<br>State, City, Zip code</div>
    <div class="contact-col contact-phone">M : 000-000-000<br>F  : 000-000-000</div>
    <div class="contact-col contact-web">www.webname.com<br>name@domainname.com</div>
  </div>
</div>
</body>
</html>
```